Company Website

Our company teaches Federal Accredited EMT certification. Our company name is Corvane Training Group. (logo is in the files). We have a current website that needs an overhaul (www.corvanetraininggroup.com). This website needs to able to be used on wordpress. We need a website that has a good flow and design, have a page that has our instructor bio’s, a page on our class information, prerequisites, and how many seats are left in the class, a page that will accept payments and layout our cost. Be able to expand as our company expands to other classes (CPR ETC.)

Target Market(s)

People that want to take an EMT class

Coding

Coded - Design and coding required

Number of Pages Required

3 page

Requirements
Must have
• A page explaining who we are, a page of the services we offer with the ability to pay using Quidora or some external source, and a page about who the instructors are.
Nice to have
• Good flow, easy to change as the Business grows

```html
<!DOCTYPE html>
<html lang="en">
<head>
<meta charset="UTF-8">
<title>Corvane Training Group</title>
<link href="https://fonts.googleapis.com/css2?family=Jost:wght@400;500;600&family=Montserrat:wght@400;500;600;700&display=swap" rel="stylesheet">
<style>
:root{
  --navy:#232b33;
  --navy-deep:#1b2228;
  --red:#d42a2f;
  --red-dark:#b81f24;
  --teal:#2fb39d;
  --ink:#2a2a2a;
  --muted:#555c63;
  --light:#ececec;
  --paper:#f4f4f4;
  --white:#ffffff;
  --line:#c9c9c9;
}
*{box-sizing:border-box;margin:0;padding:0}
html,body{width:1200px;height:4412px;overflow:hidden}
body{position:relative;font-family:"Montserrat",sans-serif;color:var(--ink);background:var(--white)}
.abs{position:absolute}

/* header */
.site-header{left:0;top:0;width:1200px;height:90px;background:var(--navy)}
.brand{display:flex;align-items:center;gap:12px}
.brand-dot{width:30px;height:30px;border-radius:50%;background:var(--red)}
.brand-name{font-weight:600;color:var(--white);font-size:20px;letter-spacing:.3px}
.nav{left:555px;top:0;height:90px;display:flex;align-items:center}
.nav a{color:#e3e6e8;text-decoration:none;font-size:15px;font-weight:500;margin-right:38px}
.nav-contact{left:943px;top:22px;width:193px;height:46px;border-radius:23px;background:#5b6570;color:#fff;font-size:15px;font-weight:500;display:flex;align-items:center;justify-content:center}

/* hero */
.hero-media{left:0;top:90px;width:1200px;height:700px;
  background:
    radial-gradient(ellipse 170px 110px at 620px 340px,rgba(255,255,255,.85),rgba(255,255,255,0) 100%),
    radial-gradient(ellipse 230px 60px at 640px 420px,rgba(214,64,52,.75),rgba(214,64,52,0) 100%),
    radial-gradient(ellipse 120px 40px at 760px 470px,rgba(255,60,60,.55),rgba(255,60,60,0) 100%),
    radial-gradient(ellipse 260px 200px at 1050px 260px,rgba(190,225,225,.7),rgba(190,225,225,0) 100%),
    radial-gradient(ellipse 180px 160px at 180px 220px,rgba(120,200,190,.5),rgba(120,200,190,0) 100%),
    linear-gradient(180deg,#1f4a4e 0%,#3f7c7e 30%,#2d5d61 55%,#1a2f33 80%,#16262a 100%)}
.hero-title{left:0;top:538px;width:1200px;text-align:center;color:#fff;font-family:"Jost",sans-serif;font-size:60px;line-height:70px;font-weight:400;text-shadow:0 2px 8px rgba(0,0,0,.35)}
.hero-title b{font-weight:600;letter-spacing:-1px}
.arrow-circle{width:70px;height:70px;border:3px solid #fff;border-radius:50%}

/* welcome */
.welcome-media{left:80px;top:870px;width:440px;height:310px;
  background:
    radial-gradient(ellipse 90px 60px at 340px 200px,rgba(90,60,160,.9),rgba(90,60,160,0) 100%),
    radial-gradient(ellipse 120px 90px at 140px 80px,rgba(190,70,50,.85),rgba(190,70,50,0) 100%),
    radial-gradient(ellipse 150px 80px at 250px 210px,rgba(200,90,80,.8),rgba(200,90,80,0) 100%),
    radial-gradient(ellipse 180px 60px at 260px 270px,rgba(0,0,0,.12),rgba(0,0,0,0) 100%)}
.welcome-title{left:565px;top:890px;font-weight:700;font-size:31px;line-height:41px;color:#1c1c1c;letter-spacing:-.6px}
.red-rule{height:3px;background:var(--red)}
.welcome-text{left:565px;top:1003px;width:505px;font-size:12px;line-height:24px;color:#333}
.btn-red{background:var(--red);color:#fff;border-radius:24px;display:flex;align-items:center;justify-content:center;font-weight:600}

/* services */
.services{left:0;top:1315px;width:1200px;height:800px;background:var(--light)}
.section-title{font-family:"Jost",sans-serif;font-weight:500;color:#1f1f1f;text-align:center}
.service-card{top:1545px;width:312px;height:252px;background:#f7f7f7;border:1px solid #d6d6d6;box-shadow:0 2px 6px rgba(0,0,0,.12);text-align:center}
.service-icon{position:absolute;left:108px;top:-48px;width:96px;height:96px;border-radius:50%;background:var(--navy);display:flex;align-items:center;justify-content:center}
.service-card h3{margin-top:73px;color:var(--red);font-family:"Jost",sans-serif;font-weight:500;font-size:16px}
.service-card p{margin:10px auto 0;width:240px;font-size:12.5px;line-height:19px;color:#444}
.btn-outline{margin:17px auto 0;width:150px;height:38px;border:2px solid #7a8087;border-radius:20px;display:flex;align-items:center;justify-content:center;font-family:"Jost",sans-serif;font-size:14px;color:#333}
.query-text{left:160px;top:1862px;font-family:"Jost",sans-serif;font-size:27px;line-height:44px;color:#222}
.query-text .phone{color:var(--teal);font-weight:500;font-size:32px}

/* teaching */
.teach-media{left:140px;top:2218px;width:414px;height:414px;border-radius:50%;
  background:
    radial-gradient(ellipse 90px 30px at 150px 150px,rgba(120,170,255,.9),rgba(120,170,255,0) 100%),
    radial-gradient(ellipse 60px 90px at 270px 90px,rgba(240,240,230,.85),rgba(240,240,230,0) 100%),
    radial-gradient(ellipse 170px 90px at 170px 280px,rgba(235,238,240,.95),rgba(235,238,240,0) 100%),
    radial-gradient(ellipse 110px 80px at 330px 330px,rgba(20,28,34,.9),rgba(20,28,34,0) 100%),
    linear-gradient(160deg,#4d5f6a 0%,#2f3d46 45%,#1d262c 100%)}
.teach-title{left:608px;top:2305px;width:470px;font-weight:700;font-size:19.5px;line-height:29px;color:#fff;letter-spacing:-.3px}
.teach-text{left:608px;top:2435px;width:470px;font-size:12px;line-height:24px;color:#fff}

/* seats band */
.seats-title{left:130px;top:2765px;width:420px;text-align:center;font-weight:600;font-size:42px;color:#fff}
.btn-white{background:#fff;border-radius:20px;display:flex;align-items:center;justify-content:center}

/* testimonial */
.testimonial{left:0;top:2925px;width:1200px;height:540px;background:#f6f6f6}
.testi-photo{left:262px;top:3081px;width:162px;height:162px;border-radius:50%;
  background:
    radial-gradient(ellipse 50px 62px at 85px 80px,#c9946f,rgba(201,148,111,0) 100%),
    radial-gradient(ellipse 70px 40px at 80px 150px,#5a4a40,rgba(90,74,64,0) 100%),
    linear-gradient(135deg,#eef0f1 0%,#d9dcde 100%)}
.testi-card{left:365px;top:3136px;width:478px;height:220px;background:#fff;box-shadow:0 8px 24px rgba(0,0,0,.08);text-align:center}
.testi-card p{margin:70px auto 0;width:300px;font-size:14px;line-height:24px;color:#444}
.testi-name{margin-top:6px;font-family:"Jost",sans-serif;font-size:20px;color:var(--red)}
.testi-nav{top:3309px;width:46px;height:46px;display:flex;align-items:center;justify-content:center}

/* contact */
.contact{left:0;top:3465px;width:1200px;height:600px;background:#f1f1f1}
.field{width:316px;height:47px;border:2px solid #cfcfcf;background:#fff;font-size:16px;color:#555;padding:14px 18px 0}

/* footer */
.footer-heading{font-weight:600;font-size:15px;color:#d5d9dc}
.footer-links{left:544px;top:4153px;list-style:none}
.footer-links li{font-size:13.5px;line-height:27px;color:#d3d7da}
.social{width:32px;height:32px;border:1.5px solid #c9ced2;border-radius:50%}
</style>
</head>
<body>

<header class="abs site-header">
  <div class="abs brand" style="left:55px;top:30px">
    <span class="brand-dot"></span><span class="brand-name">Corvane Training Group</span>
  </div>
  <nav class="abs nav">
    <a>HOME</a><a>ABOUT</a><a style="margin-right:40px">EMT CLASS</a><a>BLOG</a>
  </nav>
  <div class="abs nav-contact">CONTACT WITH US</div>
</header>

<div class="abs hero-media" role="img" aria-label="Ambulance with lights on driving through a teal-lit tunnel at speed"></div>
<svg class="abs" style="left:0;top:640px" width="1200" height="160" viewBox="0 0 1200 160">
  <path d="M0 45 Q600 210 1200 40 L1200 160 L0 160Z" fill="#fff"/>
  <path d="M0 45 Q600 210 1200 40" fill="none" stroke="#55626d" stroke-width="10"/>
  <path d="M0 52 Q600 220 1200 47 L1200 160 L0 160Z" fill="#fff"/>
</svg>
<div class="abs arrow-circle" style="left:83px;top:355px"></div>
<svg class="abs" style="left:83px;top:355px" width="70" height="70"><path d="M40 22 L27 35 L40 48" fill="none" stroke="#fff" stroke-width="4" stroke-linecap="round"/></svg>
<div class="abs arrow-circle" style="left:1047px;top:355px"></div>
<svg class="abs" style="left:1047px;top:355px" width="70" height="70"><path d="M30 22 L43 35 L30 48" fill="none" stroke="#fff" stroke-width="4" stroke-linecap="round"/></svg>
<h1 class="abs hero-title"><b>Emergency</b> Medical<br>Technicians</h1>

<div class="abs welcome-media" role="img" aria-label="Red trauma shears beside a blue medical cross emblem"></div>
<h2 class="abs welcome-title">WELCOME TO<br>CORVANE TRAINING GROUP</h2>
<div class="abs red-rule" style="left:565px;top:985px;width:100px"></div>
<p class="abs welcome-text">Emergency Medical Technicians or EMTs provide basic emergency medical care and transportation for critical and emergent patients who access the emergency medical system. This individual possess the basic knowledge and skills necessary to provide patient care and transportation. Emergency Medical Technicians function as part of a comprehensive EMS response.</p>
<div class="abs btn-red" style="left:567px;top:1165px;width:172px;height:45px;font-size:16px">Learn More</div>

<section class="abs services"></section>
<h2 class="abs section-title" style="left:0;top:1395px;width:1200px;font-size:42px">Services Offered?</h2>

<div class="abs service-card" style="left:107px">
  <div class="service-icon"><svg width="44" height="44" viewBox="0 0 44 44" fill="none" stroke="#fff" stroke-width="2"><circle cx="22" cy="14" r="8"/><path d="M22 9v10M19 11h5a2 2 0 010 4h-4a2 2 0 000 4h5"/><path d="M4 34h8l8 4h10l10-8-3-2-9 5h-7"/></svg></div>
  <h3>CORVANE TRAINING GROUP</h3>
  <p>Lorem Ipsum is simply dummy text of the printing and typesetting industry. Lorem Ipsum has been</p>
  <div class="btn-outline">LEARN MORE</div>
</div>
<div class="abs service-card" style="left:443px">
  <div class="service-icon"><svg width="44" height="44" viewBox="0 0 44 44" fill="none" stroke="#fff" stroke-width="2"><rect x="10" y="6" width="24" height="32" rx="2"/><path d="M15 14h14M15 20h14M15 26h14M15 32h8"/></svg></div>
  <h3>HIGH QUALITY TRAINING</h3>
  <p>Lorem Ipsum is simply dummy text of the printing and typesetting industry. Lorem Ipsum has been</p>
  <div class="btn-outline">LEARN MORE</div>
</div>
<div class="abs service-card" style="left:781px">
  <div class="service-icon"><svg width="44" height="44" viewBox="0 0 44 44" fill="none" stroke="#fff" stroke-width="2"><circle cx="22" cy="16" r="9"/><path d="M6 28l8-4 8 6 8-6 8 4M12 34l10 4 10-4"/></svg></div>
  <h3>JOINING OUR CLASS</h3>
  <p>Lorem Ipsum is simply dummy text of the printing and typesetting industry. Lorem Ipsum has been</p>
  <div class="btn-outline">LEARN MORE</div>
</div>

<p class="abs query-text">If you want to know more, submit a query<br>or call <span class="phone">555 0142 377</span></p>
<div class="abs btn-red" style="left:847px;top:1880px;width:209px;height:50px;border-radius:25px;font-family:'Jost',sans-serif;font-size:22px;font-weight:500">Sent Request</div>

<svg class="abs" style="left:0;top:2080px" width="1200" height="645" viewBox="0 0 1200 645" role="img" aria-label="Dark tunnel scene with an ambulance in motion">
  <defs>
    <linearGradient id="teachBg" x1="0" y1="0" x2="1" y2="1"><stop offset="0" stop-color="#44555d"/><stop offset=".5" stop-color="#2b363c"/><stop offset="1" stop-color="#1a2125"/></linearGradient>
    <radialGradient id="teachGlow" cx=".72" cy=".45" r=".35"><stop offset="0" stop-color="#6b7d84" stop-opacity=".55"/><stop offset="1" stop-color="#6b7d84" stop-opacity="0"/></radialGradient>
  </defs>
  <path d="M0 105 Q600 -50 1200 105 L1200 645 L0 645Z" fill="url(#teachBg)"/>
  <path d="M0 105 Q600 -50 1200 105 L1200 645 L0 645Z" fill="url(#teachGlow)"/>
  <path d="M0 95 Q600 -62 1200 95" fill="none" stroke="#8d9398" stroke-width="2"/>
</svg>
<div class="abs teach-media" role="img" aria-label="Police car and ambulance with emergency lights at a scene"></div>
<svg class="abs" style="left:140px;top:2218px" width="420" height="414" viewBox="0 0 420 414">
  <path d="M300 22 A207 207 0 0 1 300 392" fill="none" stroke="#d42a2f" stroke-width="4"/>
</svg>
<h2 class="abs teach-title">WE TEACH FEDERAL ACCREDITED EMT, CPR, AND CONTINUING EDUCATION CLASSES FOR BOTH ALS AND BLS PROVIDERS.</h2>
<div class="abs" style="left:608px;top:2410px;width:100px;height:2px;background:#fff"></div>
<p class="abs teach-text">Our passion is to give high quality training to those that help others. Here at Corvane Training Group we care about your success. Let us help you in the many different training opportunities available.</p>

<div class="abs" style="left:0;top:2720px;width:1200px;height:205px;background:var(--navy)"></div>
<svg class="abs" style="left:0;top:2720px" width="1200" height="205" role="img" aria-label="Row of ambulances under a red tint">
  <defs><linearGradient id="seatRed" x1="0" y1="0" x2="1" y2="1"><stop offset="0" stop-color="#c42a2f"/><stop offset=".6" stop-color="#b92329"/><stop offset="1" stop-color="#cc3338"/></linearGradient></defs>
  <polygon points="530,0 1200,0 1200,205 630,205" fill="url(#seatRed)"/>
</svg>
<div class="abs seats-title">15 Seats Left!!</div>
<div class="abs btn-white" style="left:220px;top:2840px;width:250px;height:40px;color:var(--red);font-size:17px">Explore Our EMT Class</div>
<div class="abs" style="left:660px;top:2782px;width:416px;text-align:center;color:#fff;font-weight:600;font-size:18px">February-2021-EMT-Schedule-1</div>
<div class="abs btn-white" style="left:782px;top:2835px;width:171px;height:38px;color:var(--red);font-size:14px;font-weight:600">Download Now</div>

<section class="abs testimonial"></section>
<h2 class="abs section-title" style="left:0;top:3008px;width:1200px;font-size:38px">Testimonial</h2>
<div class="abs red-rule" style="left:560px;top:3066px;width:120px"></div>
<div class="abs testi-card">
  <svg style="position:absolute;left:212px;top:-6px" width="56" height="46" viewBox="0 0 56 46" fill="none" stroke="#d42a2f" stroke-width="2.5"><path d="M24 4C12 8 4 16 4 28v14h18V26H12c0-8 5-13 12-16z"/><path d="M52 4C40 8 32 16 32 28v14h18V26H40c0-8 5-13 12-16z"/></svg>
  <p>Lorem ipsum dolor sit amet, consectetur adipiscing elit, sed do eiusmod tempor incididunt ut labore et dolore magna dolore aliqua.</p>
  <div class="testi-name">Dana Whitlock</div>
</div>
<div class="abs testi-photo" role="img" aria-label="Portrait of a smiling student"></div>
<div class="abs testi-nav" style="left:798px;background:#fff;box-shadow:0 2px 6px rgba(0,0,0,.15)"><svg width="14" height="14"><path d="M9 2 L4 7 L9 12" fill="none" stroke="#222" stroke-width="2.5"/></svg></div>
<div class="abs testi-nav" style="left:844px;background:var(--navy)"><svg width="14" height="14"><path d="M5 2 L10 7 L5 12" fill="none" stroke="#fff" stroke-width="2.5"/></svg></div>

<section class="abs contact"></section>
<h2 class="abs section-title" style="left:0;top:3535px;width:1200px;font-size:42px">Get In Touch</h2>
<div class="abs field" style="left:273px;top:3618px">Your Name</div>
<div class="abs field" style="left:611px;top:3618px">Subject</div>
<div class="abs field" style="left:273px;top:3690px">Email Address</div>
<div class="abs field" style="left:273px;top:3762px">Phone</div>
<div class="abs field" style="left:611px;top:3690px;height:119px"></div>
<div class="abs" style="left:516px;top:3845px;width:169px;height:48px;border-radius:24px;background:var(--navy);color:#fff;font-weight:600;font-size:15px;display:flex;align-items:center;justify-content:center">LEARN MORE</div>

<svg class="abs" style="left:0;top:3975px" width="1200" height="437" viewBox="0 0 1200 437">
  <path d="M0 110 Q600 -70 1200 110 L1200 437 L0 437Z" fill="#232b33"/>
</svg>
<div class="abs brand" style="left:132px;top:4128px">
  <span class="brand-dot" style="width:34px;height:34px"></span><span class="brand-name" style="font-size:22px">Corvane Training Group</span>
</div>
<p class="abs" style="left:132px;top:4236px;font-size:13px;color:#c9ced2">© 2020 Ridgeway Studio. All Rights are Reserved.</p>
<div class="abs social" style="left:136px;top:4284px"></div>
<div class="abs social" style="left:176px;top:4284px"></div>
<div class="abs social" style="left:216px;top:4284px"></div>
<div class="abs social" style="left:256px;top:4284px"></div>

<h4 class="abs footer-heading" style="left:544px;top:4103px">QUICK LINKS</h4>
<ul class="abs footer-links">
  <li>Home</li><li>About Us</li><li>EMT Class</li><li>Blog</li><li>Team</li><li>How its works</li><li>Contact Us</li>
</ul>

<h4 class="abs footer-heading" style="left:725px;top:4103px">SIGN UP FOR NEWSLETTER</h4>
<p class="abs" style="left:725px;top:4155px;width:370px;font-size:13px;line-height:20px;color:#c9ced2">If you are interested in joining our class, or have any questions please send us a message.</p>
<div class="abs" style="left:725px;top:4225px;width:310px;height:44px;border:1.5px solid #8d959c;border-radius:22px"></div>
<div class="abs" style="left:753px;top:4238px;font-size:14px;color:#aeb5ba">Email address</div>
<div class="abs" style="left:920px;top:4228px;width:112px;height:38px;border-radius:0 19px 19px 0;background:#4c565f;color:#fff;font-size:14px;display:flex;align-items:center;justify-content:center">Subscribe</div>
<div class="abs btn-red" style="left:725px;top:4290px;width:310px;height:45px;font-size:13px;font-weight:600">SCHEDULE FREE 15 MIN CONSULTATION</div>

</body>
</html>
```